Catastrophe & Disaster Mitigation & Repairs

1. Fire/smoke & flood/water & wind damage restoration for residential, commercial or industrial structure &/or content.

2. 24/7 emergency service

3. Flood, catastrophe & storm emergency response

4. Emergency board ups.

5. Specializing in insurance claims with direct insurance billing (when applicable).

6. Full service restoration. We handle everything from cleaning & deoderization of content & structure, demo, drying, disposal & dry cleaning to temporary storage, emergency electrical & plumbing & FULL repairs "To Restore residential or commercial property & content to pre loss condition".

7. Please see our website, brochure or simply ask any of our technicians for complete list of services & specialized services that we provide.

However within 60 to 90 days after we incorporate & launch this new business we are starting a sister company that will handle all of the carpentry & construction on all of our insurance jobs as well as market for additional roofing, siding, interiors, exterior, kitchens, baths, additions, painting, insulation, drywall, doors, windows, decks, additions, garages, general contracting, electrical, hardwood floor restoration & instalation, custom tile, vinyl, carpet & laminate flooring installation, tree houses, small concrete repairs, brick repair, doors, windows, new builds, etc, etc. When the time comes I will need business card, rak cards, note books, stickers, yard signs, vehicle magnets, etc for that business (Steadfast Building Services) too. So please keep in mind that we can temporarily have construction & full repairs on this card but in the near future the majority of anything carpentry or construction related (aside from demo) will need to be easily removes from this card and replaced with a brief line referring to the sister company.

We have a long long long list of services that we provide for residential, commercial & industrial. Duct cleaning & sanitize, foreclosure clean out, pre & post rental or sale cleaning &/or repairs & painting, home & office cleaning services, post construction clean up, crime scene remediation, smoke & odor removal & mitigation, residential cleaning, commercial cleaning, water proofing, biohazard clean up, septic back up clean up, temporary power, temporary heat, temporary storage, temporary repairs, refrigerant & desiccant & heat drying, mold mitigation (we don't like mold & don't advertise for mold but are educated, trained & equipped to do it upon request or nessecity), full pack out of content, full move back, demo & disposal, indoor air quality testing, consulting, claim negotiation with insurance carrier, content cleaning & restoration, jewelry cleaning, dry cleaning, pressure washing, steam pressure washing, sand & dry ice blasting, graffiti removal, inventory of damaged, destroyed & cleaned content, upholstery & carpet cleaning, grout cleaning, property winterizing, soda blasting, art & document restoration, emergency & long term utility reactivate,
landscaping & clean up of property/yard damaged as result of catastrophe (if covered in policy or upon request), wind or catastorphe damaged tree cut up & removal, project management or consulting, some equipment rental, pump outs, water extraction, electronics cleaning, bat guanno removal & mitigation, mitigation & remediation planning, detailed & itemized written estimates with industry standard pricing software, spring cleaning, hordar clean outs, garage/attic/basement & barn clean out & hauloff, RV clean out, full demo & removal of total loss or condemned structures, no intrest payment plans for the unfortunate & uninsured (with sizeable down payment). I know there are more services that I'm not thinking of too.

When a less than once in a lifetime castorphe strikes a home, business, commercial or industrial structure & often times the content of that structure the owners are often in shock & don't know what direction to turn or where to begin simply because they most likely have never been through a loss of that magnitude & in very unfamiliar territory. The amount of planning, equipment, training, networking, resources, subcontractors, manpower, financing & paperwork can be mindboggling. Especially when the majority of them have jobs, school, family & lives that don't stop due to their misfortune. Keystone Water & Blaze Recovery LLC handles every aspect from before the time first responders or plumbers are gone until the structure & content is restored to (or better than) preloss condition. They only thing we need from our customers is for them to provide us with material kind & color such as paint & flooring. Aside from that, our customers can go on with there lives and have as little stress & worry as possible given the circumstances. From a small over flowed sink to a large warehouse fire that sets of a high pressure sprinkler system to a structure that's been completely sumburged for several days it is still uncommon territory & still requires a lot of different skilled subcontractors, specialized equipment & logistics. Its what we do every day & we have it well planned in advance, a core team of dedicated & trusted professionals that we've been colleges & friends with for years. The homeowners are still our direct customer & are consulted on every aspect of mitigation & repairs to their home, property &/or content. Our customers are free to choose what (if any) aspects of the project they handle themselves. From time to time they choose to paint their own bedroom or have a friend or family member that's a electrician, plumber or tradesman & chose to use them for that portion of their loss. Point being that even though we can handle every aspect we still work closely with our customers & even if direct insurance invoicing the policy holder/home or structure owner is still our valued customer. We also do as much as we can to get their lives back to as fully functional as possible given the circumstance.

As I'm sure you can tell.... I've provided a lot of text. Please save some for the rack cards, brochures, folders and anything else you may be able to use it in. I have a ton more of informational text from our old website. I also have a lot of testimonials, photos & anything else you may be able to implement in our promotional & informative campaign. We've been in this business for 8 years, in the flood & fire restoration business for 11 years as well as having well over 100 years combined experience in the carpentry & constructive fields. At some point & on something I'd like all our services listed. Maybe on brochures. I attached the brochure that my cousin (who at the time was graphics editor at Vortell Magazine) designed when we first got in business. Its a quality job but I feel is very outdated & not very informative.
I understand that I have just a few seconds to catch my potential customers eye so I feel with the business cards that one side needs to POP, be clean, look good and stand out at you and the other side can list some of our services. I think that #'s 1 thru 7 at the top of this section should be most of it for the back of the business card. Please look through this not so brief, brief & see what you think. I'm gearing towards fire, smoke, flood & wind mitigation. Then cleaning + emergency, storm & catastrophe response.
The biggest thing is that it needs to make both of my competitors attached cards look like shit & unfortunately I kinda like both of their cards so you have your work cut out for you. One of the reasons I gave you such extensive information. Please keep rack cards, brochures, letter heads, envelopes, notebooks, folders, informative literature, documents, stickers, door magnets & everything else we may need for both this & construction business. I'll be able to pay for that next week. I also keep clicking on Double Sided & it keeps changing back to single by itself.
Updates

PLEASE NOTE THAT I SUBMITTED FOR "BUSINESS CARD DESIGN" THERE WASNT A OPTION FOR EXACTLY WHAT I NEED HELP WITH. I NEED MY EXISTING LOGO MODIFIED ALONG WITH THE BUSINESS CARD DESIGN. I ALSO NEED A BROCHURE & RACK CARD DESIGNED. I'D LIKE TO DO ALL OF THIS ASAP. PLEASE LET ME KNOW THE CHARGES FOR THESE ADDITIONAL SERVICES. THANK YOU.

Target Market(s)

Insurance agents, insurance adjusters, homeowners/policy holders that have experienced a fire, flood or other catastorphies, plumbers, builders, etc

Industry/Entity Type

Office Cleaning

Contact Information for Business Card

Reed Talbot
Keystone Water & Blaze Recovery LLC
5318 Whitcombe Rd
Harlow Falls, NY 14092
www.keystonewaterblaze.example
reed@keystonewaterblaze.example
Office: 716.555.0142
Cell: 716.555.0187

Requirements
Must have
• I've attached a copy of our old business & logo as well as a old business card. I'd like to incorporate our old logo & colors. Or at least entertain using them in some aspect. Feel free to change it up though. Our old logo is supposed to represent a roof & the red for fire & blue for water.

My old card is cluttered & doesn't catch the eye.

The other cards I've attached are Grip on Spores who is my old business partner from years ago & Lakeshore Basin Renewal is my ex fiance so my new cards don't just need to catch the eye & be functional they need to look at least twice as good as my competitors.
Nice to have
• One side business name, my name, logo, phone #'s, email, website, fb, twitter, instagram, etc. I feel one side should be clean, bold & catch the eye in the 6 seconds I have to do so.

Then opposing side should have some of our more prominent services along with more information.

I'd like to keep away from having the business cards on white card stock. I think a color or multi color looks better.

I guess I'm open to anything. You guys are the pro's. As long as it looks great & gets the point across. I have 2 other people that need the same cards too. Just different names, emails & cell #'s. And as I stated earlier. I'm planning on ordering notepads, yard signs, rack cards, brochures, magnets & a few other things at the same time. I'll need design & layout on all of those too. Just let me know what the additional cost will be. They'll have the same colors, logo & business name. Just more or less info depending on the product.
Should not have
• ?

```html
<!DOCTYPE html>
<html lang="en">
<head>
<meta charset="utf-8">
<title>Keystone Water &amp; Blaze Recovery — Business Card</title>
<link rel="stylesheet" href="https://fonts.googleapis.com/css2?family=Source+Sans+3:wght@400;600;700&display=swap">
<style>
  :root {
    --backdrop: #dfe3e6;
    --card-white: #ffffff;
    --card-blue: #1d6fbd;
    --card-blue-deep: #155a9e;
    --fire-red: #e0262b;
    --alert-red: #ff3b3b;
    --water-blue: #1b64ae;
    --ink: #1f1f1f;
    --ink-soft: #333333;
    --on-blue: #ffffff;
  }
  * { box-sizing: border-box; margin: 0; padding: 0; }
  html, body {
    width: 1200px; height: 960px; overflow: hidden;
    background: var(--backdrop);
    font-family: "Source Sans 3", "Myriad Pro", Arial, sans-serif;
  }
  .sheet {
    width: 1200px; height: 960px;
    display: flex; flex-direction: column; align-items: center; justify-content: center;
    gap: 56px;
  }
  .card {
    width: 700px; height: 400px;
    border-radius: 6px;
    box-shadow: 0 10px 28px rgba(0,0,0,.18);
    position: relative; overflow: hidden;
  }

  /* Shared brand line */
  .brand { display: flex; align-items: center; gap: 14px; }
  .brand-mark { width: 34px; height: 34px; background: var(--fire-red); flex: none; }
  .brand-name {
    font-weight: 700; font-size: 30px; line-height: 1.05; color: var(--ink-soft);
    text-align: right;
  }

  /* Front */
  .card-front { background: var(--card-white); padding: 40px 48px; }
  .holder {
    margin-top: 38px;
    font-weight: 700; font-size: 38px; letter-spacing: .5px; line-height: 1;
  }
  .holder .first { color: var(--fire-red); }
  .holder .last { color: var(--water-blue); }
  .company { margin-top: 14px; font-weight: 600; font-size: 21px; color: var(--ink); }
  .contacts { list-style: none; margin-top: 14px; }
  .contacts li {
    display: flex; align-items: center; gap: 10px;
    font-size: 19px; color: var(--ink); line-height: 1.42;
  }
  .contacts svg { width: 17px; height: 17px; flex: none; }

  /* Back */
  .card-back {
    background: radial-gradient(ellipse at 75% 20%, #3a8ad6 0%, var(--card-blue) 45%, var(--card-blue-deep) 100%);
    color: var(--on-blue);
    display: flex; flex-direction: column; align-items: center;
    padding-top: 62px; text-align: center;
  }
  .card-back .brand-name { color: var(--on-blue); font-size: 34px; }
  .card-back .brand-mark { width: 38px; height: 38px; }
  .services {
    margin-top: 44px;
    font-weight: 700; font-size: 19px; letter-spacing: .6px; text-transform: uppercase;
  }
  .services .dot { margin: 0 8px; }
  .emergency {
    margin-top: 8px;
    font-weight: 700; font-size: 20px; letter-spacing: .8px; color: var(--alert-red);
    text-transform: uppercase;
  }
  .sectors { margin-top: 40px; font-size: 18px; letter-spacing: .6px; }
</style>
</head>
<body>
<main class="sheet">

  <section class="card card-front" aria-label="Card front">
    <div class="brand">
      <span class="brand-mark" aria-hidden="true"></span>
      <span class="brand-name">Keystone Water &amp; Blaze<br>Recovery</span>
    </div>
    <h1 class="holder"><span class="first">REED</span> <span class="last">TALBOT</span></h1>
    <p class="company">Keystone Water &amp; Blaze Recovery LLC</p>
    <ul class="contacts">
      <li>
        <svg viewBox="0 0 24 24" fill="var(--fire-red)" aria-hidden="true"><path d="M12 3 2 12h3v9h5v-6h4v6h5v-9h3z"/></svg>
        5318 Whitcombe Rd Harlow Falls, NY 14092
      </li>
      <li>
        <svg viewBox="0 0 24 24" fill="var(--fire-red)" aria-hidden="true"><path d="M6.6 10.8a15 15 0 0 0 6.6 6.6l2.2-2.2a1 1 0 0 1 1-.25 11.4 11.4 0 0 0 3.6.57 1 1 0 0 1 1 1V20a1 1 0 0 1-1 1A17 17 0 0 1 3 4a1 1 0 0 1 1-1h3.5a1 1 0 0 1 1 1c0 1.25.2 2.450 .57 3.57a1 1 0 0 1-.25 1z"/></svg>
        716.555.0142
      </li>
      <li>
        <svg viewBox="0 0 24 24" fill="none" stroke="var(--fire-red)" stroke-width="2" aria-hidden="true"><rect x="6" y="2" width="12" height="20" rx="2"/><line x1="11" y1="18" x2="13" y2="18"/></svg>
        716.555.0187
      </li>
      <li>
        <svg viewBox="0 0 24 24" fill="none" stroke="var(--fire-red)" stroke-width="2" aria-hidden="true"><rect x="3" y="5" width="18" height="14"/><path d="m3 6 9 7 9-7"/></svg>
        reed@keystonewaterblaze.example
      </li>
      <li>
        <svg viewBox="0 0 24 24" fill="none" stroke="var(--fire-red)" stroke-width="2" aria-hidden="true"><circle cx="12" cy="12" r="9"/><path d="M3 12h18M12 3c3 3 3 15 0 18M12 3c-3 3-3 15 0 18"/></svg>
        www.keystonewaterblaze.example
      </li>
    </ul>
  </section>

  <section class="card card-back" aria-label="Card back">
    <div class="brand">
      <span class="brand-mark" aria-hidden="true"></span>
      <span class="brand-name">Keystone Water &amp; Blaze<br>Recovery</span>
    </div>
    <p class="services">Fire/Smoke<span class="dot">•</span>Flood/Water<span class="dot">•</span>Wind Damage Restoration</p>
    <p class="emergency">24/7 Emergency Service</p>
    <p class="sectors">residential • commercial • industrial</p>
  </section>

</main>
</body>
</html>
```